Chips Sachet pack Design

I would like to design a new 60 grams Sachet pack for plantain chips , customizing the existing product identity as attached .
The following should be consistent with with the existing pack :
- Fonts and color scheme
I will provide a new brand logo for our brand

Target Market(s)

The product is sold in Retail stores

Industry/Entity Type

FMCG

Requirements
Must have
• Similar identity to existing packs and brand as attached
Nice to have
• Similar design to the attached desired concept

```html
<!DOCTYPE html>
<html lang="en">
<head>
<meta charset="utf-8">
<title>Plantain Chips 60gm Sachet</title>
<link href="https://fonts.googleapis.com/css2?family=Lilita+One&family=Marcellus&family=Montserrat:wght@500;700&family=Fjalla+One&family=Kaushan+Script&display=swap" rel="stylesheet">
<style>
  :root {
    --pack-green: #00a651;
    --deep-green: #1f5e33;
    --stripe-green: #4f8a63;
    --label-white: #ffffff;
    --label-yellow: #f4e300;
    --banner-yellow: #f2e60c;
    --ribbon-beige: #d6b0a0;
    --ribbon-orange: #e0552a;
    --frame-brown: #a77460;
    --chip-gold: #e6b43a;
    --chip-light: #f3d36a;
    --badge-red: #9b1a1a;
    --badge-tan: #e2bd6a;
    --ink: #111111;
    --natural-red: #e3161b;
  }
  html, body {
    margin: 0;
    padding: 0;
    width: 1200px;
    height: 921px;
    overflow: hidden;
    background: #ffffff;
  }
  .sachet-front {
    position: absolute;
    left: 312px;
    top: 30px;
    width: 575px;
    height: 860px;
  }
  .display { font-family: "Lilita One", sans-serif; }
  .serif-sub { font-family: "Marcellus", serif; }
  .sans { font-family: "Montserrat", sans-serif; }
  .condensed { font-family: "Fjalla One", sans-serif; }
  .script { font-family: "Kaushan Script", cursive; }
</style>
</head>
<body>
<svg class="sachet-front" viewBox="0 0 865 1293" xmlns="http://www.w3.org/2000/svg">
  <defs>
    <linearGradient id="chip-tones" x1="0" y1="0" x2="1" y2="1">
      <stop offset="0" stop-color="var(--chip-light)"/>
      <stop offset="0.5" stop-color="var(--chip-gold)"/>
      <stop offset="1" stop-color="#d99a2b"/>
    </linearGradient>
  </defs>

  <!-- pack background -->
  <rect class="pack-body" width="865" height="1293" fill="var(--pack-green)"/>

  <!-- product photo window -->
  <path class="photo-frame" d="M0 620 Q432 500 865 620 L865 1000 Q432 1115 0 1040 Z" fill="var(--frame-brown)"/>
  <path class="product-photo" role="img" aria-label="Photo of golden fried plantain chips"
        d="M0 635 Q432 518 865 635 L865 985 Q432 1098 0 1025 Z" fill="url(#chip-tones)"/>

  <!-- title label -->
  <g class="title-label">
    <path d="M160 180 L185 180 L185 150 L680 150 L680 180 L705 180 L690 325 L640 325 L595 445 L275 445 L230 325 L180 325 Z" fill="var(--deep-green)"/>
    <path d="M172 188 L195 188 L195 160 L670 160 L670 188 L692 188 L680 318 L632 318 L588 435 L282 435 L238 318 L188 318 Z" fill="var(--label-yellow)"/>
    <path d="M180 194 L202 194 L202 168 L662 168 L662 194 L684 194 L673 312 L627 312 L583 427 L287 427 L243 312 L194 312 Z" fill="var(--label-white)"/>
    <g class="label-stripes">
      <polygon points="235,140 330,140 320,165 225,165" fill="var(--stripe-green)"/>
      <polygon points="240,160 320,160 312,172 235,172" fill="var(--label-yellow)"/>
      <polygon points="205,165 315,165 308,190 200,190" fill="var(--stripe-green)"/>
      <polygon points="535,140 630,140 640,165 545,165" fill="var(--stripe-green)"/>
      <polygon points="545,160 625,160 632,172 552,172" fill="var(--label-yellow)"/>
      <polygon points="550,165 660,165 665,190 557,190" fill="var(--stripe-green)"/>
      <rect x="210" y="212" width="120" height="5" fill="var(--stripe-green)"/>
      <rect x="535" y="212" width="120" height="5" fill="var(--stripe-green)"/>
    </g>
    <circle cx="338" cy="168" r="8" fill="var(--deep-green)"/>
    <text class="sans brand-name" x="440" y="182" text-anchor="middle" font-size="44" font-weight="700" fill="var(--deep-green)">Leafora</text>
    <text class="sans brand-tagline" x="440" y="215" text-anchor="middle" font-size="12" font-weight="500" fill="var(--ink)" letter-spacing="1">QUALITY SINCE XXXX</text>
    <text class="display product-name" x="435" y="298" text-anchor="middle" font-size="84" fill="var(--deep-green)">PLANTAIN</text>
    <text class="display product-name" x="432" y="295" text-anchor="middle" font-size="84" fill="var(--ink)">PLANTAIN</text>
    <text class="display product-name" x="435" y="378" text-anchor="middle" font-size="84" fill="var(--deep-green)">CHIPS</text>
    <text class="display product-name" x="432" y="375" text-anchor="middle" font-size="84" fill="var(--ink)">CHIPS</text>
    <circle cx="256" cy="326" r="6" fill="var(--stripe-green)"/>
    <circle cx="610" cy="326" r="6" fill="var(--stripe-green)"/>
    <text class="serif-sub product-spanish" x="435" y="420" text-anchor="middle" font-size="34" fill="var(--ink)">PLATANITOS</text>
  </g>

  <!-- healthy snacks badge -->
  <g class="healthy-badge">
    <path d="M670 410 Q690 360 750 365 Q790 370 780 420 Q775 475 720 475 Q660 470 670 410 Z" fill="#f0c26a"/>
    <path d="M676 410 Q694 368 750 372 Q784 378 774 420 Q768 467 720 468 Q668 462 676 410 Z" fill="var(--badge-red)"/>
    <text class="script" x="728" y="410" text-anchor="middle" font-size="24" fill="#f28a5a">healthy</text>
    <text class="script" x="745" y="452" text-anchor="middle" font-size="34" fill="#ffffff">Snacks</text>
  </g>

  <!-- flavour ribbon -->
  <g class="flavour-ribbon">
    <polygon points="205,535 275,510 345,630 240,630" fill="var(--ribbon-beige)"/>
    <polygon points="650,525 580,500 510,615 600,600" fill="var(--ribbon-beige)"/>
    <polygon points="300,575 345,610 340,570" fill="var(--ribbon-orange)"/>
    <polygon points="560,575 510,610 520,570" fill="var(--ribbon-orange)"/>
    <rect x="265" y="475" width="325" height="105" fill="var(--banner-yellow)"/>
    <text class="display" x="428" y="535" text-anchor="middle" font-size="62" fill="var(--ink)">SALTED</text>
    <text class="sans" x="428" y="568" text-anchor="middle" font-size="30" font-weight="700" fill="var(--ink)">Saladitos</text>
  </g>

  <!-- zero trans fat flag -->
  <g class="trans-fat-flag">
    <path d="M0 975 Q0 965 15 965 L170 965 L170 1045 Q170 1060 150 1060 L0 1068 Z" fill="#f9c513"/>
    <text class="condensed" x="28" y="1045" text-anchor="middle" font-size="72" fill="var(--ink)">0</text>
    <text class="condensed" x="103" y="1003" text-anchor="middle" font-size="28" fill="var(--ink)">Trans Fat</text>
    <text class="condensed" x="103" y="1037" text-anchor="middle" font-size="28" fill="var(--ink)">Cholesterol</text>
  </g>

  <!-- natural badge -->
  <g class="natural-badge">
    <path d="M220 1075 Q215 1020 270 1010 Q330 1005 340 1060 Q345 1110 285 1110 Q225 1112 220 1075 Z" fill="var(--badge-tan)" stroke="#1c8a3c" stroke-width="3"/>
    <text class="sans" x="285" y="1060" text-anchor="middle" font-size="24" font-weight="700" fill="#ffffff">100%</text>
    <text class="sans" x="295" y="1090" text-anchor="middle" font-size="24" font-weight="700" fill="var(--natural-red)">NATURAL</text>
  </g>

  <text class="sans net-weight" x="432" y="1168" text-anchor="middle" font-size="31" font-weight="500" fill="#1d2b22">Net Weight 60gm</text>
</svg>
</body>
</html>
```